Brightwell Pictures Business Card

Hello,

i would like to have a dynamic, creative but tasteful card, colour used, front and back. I have attached a sample card that I liked very much from another individual to give you an idea of the theme/approach, but not colour. Ideally the graphic elements of the Brightwell Logo are brought into the design.

Target Market(s)

North America

Industry/Entity Type

Film Production

Contact Information for Business Card

Mirela Vantasch
President/Founder
Brightwell Pictures Inc.
587 914 3362
mirela@brightwellpix.tv

Font styles to use
Sans Serif

Colors
6b449b
5c5c5c
fdfdfd
000000

Requirements
Must have
• Logo, name, Company name, email and cell number. no Address line to be included.
Should not have
• any unrelated GFX elements, serif fonts

```html
<!DOCTYPE html>
<html lang="en">
<head>
<meta charset="utf-8">
<title>Brightwell Pictures Business Card</title>
<link rel="stylesheet" href="https://fonts.googleapis.com/css2?family=Roboto:wght@400;700&display=swap">
<style>
  :root {
    --brand-purple: #6b449b;
    --brand-purple-soft: #7553a4;
    --brand-purple-deep: #643f93;
    --paper-white: #fdfdfd;
    --backdrop: #e9e7ec;
    --ink-grey: #5c5c5c;
  }
  * { box-sizing: border-box; margin: 0; padding: 0; }
  html, body {
    width: 1200px;
    height: 1200px;
    overflow: hidden;
  }
  body {
    position: relative;
    background: var(--backdrop);
    font-family: "Roboto", Arial, sans-serif;
    color: var(--paper-white);
  }
  .card {
    position: absolute;
    left: 213px;
    width: 774px;
    height: 442px;
    overflow: hidden;
    box-shadow: 0 6px 18px rgba(0, 0, 0, 0.18);
  }
  .card--front {
    top: 149px;
    background: var(--brand-purple);
  }
  .card--back {
    top: 633px;
    background: var(--brand-purple);
  }
  .brand-pattern {
    position: absolute;
    inset: 0;
  }
  .brand-pattern--front {
    background: radial-gradient(circle 400px at 50% 50%,
      var(--brand-purple) 0%,
      var(--brand-purple) 36%,
      var(--paper-white) 60%,
      var(--paper-white) 90%,
      var(--brand-purple) 100%);
  }
  .brand-pattern--back {
    background: radial-gradient(circle 400px at 50% 50%,
      var(--brand-purple-deep) 0%,
      var(--brand-purple) 40%,
      var(--brand-purple-soft) 70%,
      var(--brand-purple-soft) 90%,
      var(--brand-purple) 100%);
  }
  .contact-block {
    position: absolute;
    left: 0;
    right: 0;
    top: 128px;
    text-align: center;
  }
  .contact-name {
    font-size: 30px;
    font-weight: 700;
    line-height: 36px;
    letter-spacing: 0.2px;
  }
  .contact-role,
  .contact-company {
    font-size: 20px;
    font-weight: 400;
    line-height: 28px;
  }
  .contact-divider {
    width: 44px;
    height: 3px;
    margin: 18px auto 24px;
    background: var(--paper-white);
  }
  .contact-line {
    font-size: 19px;
    font-weight: 400;
    line-height: 26px;
  }
  .brand-lockup {
    position: absolute;
    left: 0;
    right: 0;
    top: 196px;
    display: flex;
    align-items: center;
    justify-content: center;
    gap: 16px;
  }
  .brand-mark {
    width: 34px;
    height: 34px;
    border-radius: 50%;
    background: var(--paper-white);
  }
  .brand-name {
    font-size: 50px;
    font-weight: 700;
    letter-spacing: -1px;
    line-height: 56px;
    color: var(--paper-white);
  }
</style>
</head>
<body>
  <section class="card card--front" aria-label="Business card front">
    <div class="brand-pattern brand-pattern--front" role="img" aria-label="Bold white geometric brand graphic around a purple centre"></div>
    <div class="contact-block">
      <p class="contact-name">Mirela Vantasch</p>
      <p class="contact-role">President/Founder</p>
      <p class="contact-company">Brightwell Pictures Inc</p>
      <div class="contact-divider"></div>
      <p class="contact-line">587 914 3362</p>
      <p class="contact-line">mirela@brightwellpix.tv</p>
    </div>
  </section>

  <section class="card card--back" aria-label="Business card back">
    <div class="brand-pattern brand-pattern--back" role="img" aria-label="Faint tonal geometric brand graphic"></div>
    <div class="brand-lockup">
      <span class="brand-mark" aria-hidden="true"></span>
      <p class="brand-name">brightwell pictures</p>
    </div>
  </section>
</body>
</html>
```